A stationary and business card desgn for a podiatry clinic

i require a stationary design for letter heads, envelopes, buisness cards.

it is for a new podiatry practise within a medical centre, that deals with all lower limb pathology and injury and foot related problems.

the colour scheme for my exisiting logo is orange blue and white. colours provided below.
i would like a white background for the buisness card.

the final design should portray health and wellbeing in a professional manner that still looks modern but sophisticated.

male and female, off all ethinical backgrounds aged between 30-80 years

Medical

• letter head.
need to include all contact details mentioned below.
need to also include ABN 53208741196

i prefer the logo on the top left hand corner and the contact info on the right. the address can be written in a sentence like form as the footer.

Business card
Front:

include logo provided.

clinic details on the front of the card.

Carla Westbrook
B.Pod

P: 8391 4460
F: 8391 4478
M: 0437 612 809
E: carla@velmora.com.au
W: www.velmora.com.au

(may use icons to indicate contact type)

on back

Appointments:

lines to write dates, time etc.
(3-4 of these)
and a small photo of just the foot from the logo in coloured watermark.

Address:
Larkvale Medical Centre
41 Tambrell Street
Corrindale SA 5127
(this location infomation could be in smaller font at the bottom of the buisness card under a line, running in a sentence like fashion) or in the bottom left or right hand corner in a paragraph like you would write it on an envelope

however if you think a different lay out at the back will look better by all means i just need to have room for the appointment even if it is just lines/ space.

i also prefer square cards not rounded corners.

thanks
• plain texts such as times new roman and arial

```html
<!DOCTYPE html>
<html lang="en">
<head>
<meta charset="utf-8">
<title>Velmora Podiatry – Stationery Set</title>
<link rel="stylesheet" href="https://fonts.googleapis.com/css2?family=Jost:ital,wght@0,400;0,500;0,600;1,400&display=swap">
<style>
  :root{
    --brand-blue:#2b3990;
    --brand-orange:#f26522;
    --paper:#ffffff;
    --ink:#333333;
    --ink-soft:#6d6d6d;
    --rule:#c9c9c9;
    --stage:#e4e4e4;
    --window:#f1f1f1;
  }
  *{box-sizing:border-box;margin:0;padding:0}
  html,body{width:1200px;height:808px;overflow:hidden}
  body{background:var(--stage);font-family:"Jost",Arial,sans-serif;color:var(--ink);position:relative}

  .sheet{position:absolute;background:var(--paper);box-shadow:0 2px 8px rgba(0,0,0,.18)}

  /* brand wordmark */
  .brand{display:flex;align-items:center;gap:6px;color:var(--brand-blue);font-weight:600;line-height:1;letter-spacing:.2px;white-space:nowrap;position:relative;z-index:1}
  .brand-dot{border-radius:50%;background:var(--brand-orange);flex:none}

  /* contact line shared by letterhead and envelopes */
  .contact-line{display:flex;align-items:center;gap:10px;white-space:nowrap;color:var(--ink)}
  .contact-item{display:flex;align-items:center;gap:3px}
  .icon{flex:none;display:block}
  .abn-label{color:var(--brand-orange);font-weight:600}
  .web{position:absolute;color:var(--ink);white-space:nowrap}
  .web strong{font-weight:600}
  .band{position:absolute;left:0;right:0;background:var(--brand-blue)}

  /* letterhead */
  .letterhead{left:22px;top:20px;width:546px;height:770px}
  .letterhead .brand{position:absolute;left:40px;top:44px;font-size:24px}
  .letterhead .brand-dot{width:14px;height:14px}
  .letterhead .web{right:24px;bottom:52px;font-size:9px}
  .letterhead .contact-line{position:absolute;left:28px;bottom:34px;font-size:8px}
  .letterhead .band{bottom:0;height:22px}

  /* business card */
  .card{width:252px;height:146px;top:30px;overflow:hidden}
  .card-front{left:596px}
  .card-back{left:866px}
  .card-front .brand{position:absolute;left:16px;top:22px;font-size:12px;gap:4px}
  .card-front .brand-dot{width:8px;height:8px}
  .holder{position:absolute;right:16px;top:18px;text-align:right;z-index:1}
  .holder-name{font-size:9px;font-weight:500;color:var(--ink)}
  .holder-title{font-size:6.5px;font-style:italic;color:var(--ink-soft)}
  .card-address{position:absolute;left:16px;top:58px;font-size:6.5px;line-height:1.35;z-index:1}
  .card-contacts{position:absolute;left:16px;top:88px;list-style:none;font-size:6.5px;line-height:1.45;z-index:1}
  .card-contacts li{display:flex;align-items:center;gap:4px}
  .card-watermark{position:absolute;right:10px;bottom:8px;width:88px;height:100px;border-radius:44px;z-index:0;
    background:radial-gradient(circle at 55% 40%,rgba(242,101,34,.10),rgba(43,57,144,.06) 60%,transparent 75%)}
  .appointments-title{position:absolute;left:18px;top:24px;font-size:10px;font-weight:500}
  .appointment-lines{position:absolute;left:18px;top:46px;width:128px;list-style:none;z-index:1}
  .appointment-lines li{height:20px;border-bottom:1px solid var(--rule)}

  /* envelope front */
  .envelope-front{left:596px;top:200px;width:584px;height:282px}
  .envelope-front .brand{position:absolute;left:30px;top:46px;font-size:22px}
  .envelope-front .brand-dot{width:13px;height:13px}
  .address-window{position:absolute;left:30px;top:122px;width:272px;height:80px;border-radius:14px;
    background:var(--window);box-shadow:inset 0 0 0 5px #e6e6e6}
  .envelope-front .web{right:22px;bottom:40px;font-size:8px}
  .envelope-front .contact-line{position:absolute;left:30px;bottom:26px;font-size:7.5px}
  .envelope-front .band{bottom:0;height:16px}

  /* envelope back */
  .envelope-back{left:596px;top:508px;width:584px;height:282px;overflow:hidden}
  .flap-lines{position:absolute;inset:0}
  .envelope-back .brand{position:absolute;left:50%;top:34px;transform:translateX(-50%);font-size:13px}
  .envelope-back .brand-dot{width:8px;height:8px}
  .return-address{position:absolute;right:36px;bottom:42px;font-size:7.5px;white-space:nowrap}
  .return-address .contact-line{margin-top:4px;font-size:7px;gap:8px}
</style>
</head>
<body>

<!-- Letterhead -->
<section class="sheet letterhead" aria-label="Letterhead">
  <div class="brand"><span class="brand-dot"></span>Velmora Podiatry</div>
  <p class="web"><strong>www.velmora</strong>.com.au</p>
  <div class="contact-line">
    <span>Larkvale Medical Centre 41 Tambrell Street Corrindale SA 5127</span>
    <span class="contact-item"><svg class="icon" width="8" height="8" viewBox="0 0 8 8"><circle cx="4" cy="4" r="4" fill="#f26522"/><path d="M2.6 2.2l.8.8-.4.5a3 3 0 0 0 1.5 1.5l.5-.4.8.8-.6.6C3.6 5.7 2.3 4.4 2 3z" fill="#fff"/></svg>8391 4460</span>
    <span class="contact-item"><svg class="icon" width="8" height="8" viewBox="0 0 8 8"><circle cx="4" cy="4" r="4" fill="#f26522"/><rect x="2.2" y="2.6" width="3.6" height="2.8" fill="#fff"/></svg>8391 4478</span>
    <span class="contact-item"><svg class="icon" width="8" height="8" viewBox="0 0 8 8"><rect width="8" height="8" rx="1.5" fill="#f26522"/><path d="M1.8 2.6h4.4v2.8H1.8zM1.8 2.6L4 4.3l2.2-1.7" fill="none" stroke="#fff" stroke-width=".6"/></svg>carla@velmora.com.au</span>
    <span><span class="abn-label">ABN</span> 53208741196</span>
  </div>
  <div class="band"></div>
</section>

<!-- Business card front -->
<section class="sheet card card-front" aria-label="Business card front">
  <div class="brand"><span class="brand-dot"></span>Velmora Podiatry</div>
  <div class="holder">
    <p class="holder-name">Carla Westbrook</p>
    <p class="holder-title">B.Pod</p>
  </div>
  <p class="card-address">Larkvale Medical Centre<br>41 Tambrell Street<br>Corrindale SA 5127</p>
  <ul class="card-contacts">
    <li><svg class="icon" width="6" height="6" viewBox="0 0 8 8"><circle cx="4" cy="4" r="4" fill="#f26522"/></svg>8391 4460 <svg class="icon" width="6" height="6" viewBox="0 0 8 8"><circle cx="4" cy="4" r="4" fill="#f26522"/></svg>8391 4478</li>
    <li><svg class="icon" width="6" height="6" viewBox="0 0 8 8"><rect x="1.5" width="5" height="8" rx="1" fill="#f26522"/></svg>0437 612 809</li>
    <li><svg class="icon" width="6" height="6" viewBox="0 0 8 8"><rect width="8" height="8" rx="1.5" fill="#f26522"/></svg>carla@velmora.com.au</li>
    <li><svg class="icon" width="6" height="6" viewBox="0 0 8 8"><circle cx="4" cy="4" r="4" fill="#f26522"/></svg>www.velmora.com.au</li>
  </ul>
  <div class="card-watermark" role="img" aria-label="Faint watermark of the clinic's foot mark"></div>
</section>

<!-- Business card back -->
<section class="sheet card card-back" aria-label="Business card back">
  <p class="appointments-title">Appointments</p>
  <ul class="appointment-lines"><li></li><li></li><li></li><li></li></ul>
  <div class="card-watermark" role="img" aria-label="Faint coloured watermark of the foot from the clinic mark"></div>
</section>

<!-- Envelope front -->
<section class="sheet envelope-front" aria-label="Envelope front">
  <div class="brand"><span class="brand-dot"></span>Velmora Podiatry</div>
  <div class="address-window"></div>
  <p class="web"><strong>www.velmora</strong>.com.au</p>
  <div class="contact-line">
    <span>Larkvale Medical Centre 41 Tambrell Street Corrindale SA 5127</span>
    <span class="contact-item"><svg class="icon" width="7" height="7" viewBox="0 0 8 8"><circle cx="4" cy="4" r="4" fill="#f26522"/></svg>8391 4460</span>
    <span class="contact-item"><svg class="icon" width="7" height="7" viewBox="0 0 8 8"><circle cx="4" cy="4" r="4" fill="#f26522"/></svg>8391 4478</span>
    <span class="contact-item"><svg class="icon" width="7" height="7" viewBox="0 0 8 8"><rect width="8" height="8" rx="1.5" fill="#f26522"/></svg>carla@velmora.com.au</span>
    <span><span class="abn-label">ABN</span> 53208741196</span>
  </div>
  <div class="band"></div>
</section>

<!-- Envelope back -->
<section class="sheet envelope-back" aria-label="Envelope back">
  <svg class="flap-lines" width="584" height="282" viewBox="0 0 584 282">
    <path d="M0 40 Q290 140 584 20" fill="none" stroke="#d0d0d0" stroke-width="1"/>
    <path d="M0 282 L250 150 M584 282 L350 110" fill="none" stroke="#dcdcdc" stroke-width="1"/>
  </svg>
  <div class="brand"><span class="brand-dot"></span>Velmora Podiatry</div>
  <div class="return-address">
    <p>Larkvale Medical Centre 41 Tambrell Street Corrindale SA 5127</p>
    <div class="contact-line">
      <span class="contact-item"><svg class="icon" width="6" height="6" viewBox="0 0 8 8"><circle cx="4" cy="4" r="4" fill="#f26522"/></svg>8391 4460</span>
      <span class="contact-item"><svg class="icon" width="6" height="6" viewBox="0 0 8 8"><circle cx="4" cy="4" r="4" fill="#f26522"/></svg>8391 4478</span>
      <span class="contact-item"><svg class="icon" width="6" height="6" viewBox="0 0 8 8"><rect width="8" height="8" rx="1.5" fill="#f26522"/></svg>carla@velmora.com.au</span>
    </div>
  </div>
</section>

</body>
</html>
```